Tradeshow Exhibit Background Design

Looking to make improvements on my tradeshow exhibit backdrop. I created the current design myself, and I'm not 100% happy with it. Because its a big investment, I want it to be perfect.
For context:
- The booth will be used in multiple configurations (20 ft, 10 ft, and 8 ft).
- The booth structure will include two panels that are 5' x 7.5', and one panel that is 8' x 8.5' (attached a photo of the set-up.)
- We plan on getting the double sided fabric printing so that we can use it in the various configurations (the 10' config will be the two 5' panels put together, and the 20' config will be all three.)
The design should be visually impactful from a distance but also clear and readable up close. It needs to align with our brand identity and effectively communicate what we do at a glance.
I've includes a photo example of the booth structure, my current design, as well as our company brand guidelines.

```html
<!DOCTYPE html>
<html lang="en">
<head>
<meta charset="utf-8">
<title>10 FT Configuration – Stratum Tradeshow Backdrop</title>
<link rel="stylesheet" href="https://fonts.googleapis.com/css2?family=Exo+2:wght@400;500;600;700;800&family=Open+Sans:wght@400&display=swap">
<style>
  :root {
    --brand-red: #d0262f;
    --brand-navy: #08252e;
    --brand-grey: #76808a;
    --title-ink: #0b2530;
    --sparkle: #ec8f95;
    --tagline: #c7cbd1;
    --white: #ffffff;
    --paper: #ffffff;
  }
  html, body {
    margin: 0;
    padding: 0;
    width: 1200px;
    height: 1200px;
    overflow: hidden;
    background: var(--paper);
  }
  .sheet {
    position: relative;
    width: 1200px;
    height: 1200px;
    font-family: "Exo 2", sans-serif;
  }
  .sheet-title {
    position: absolute;
    top: 72px;
    left: 0;
    width: 100%;
    margin: 0;
    text-align: center;
    font-weight: 700;
    font-size: 40px;
    letter-spacing: 0.5px;
    color: var(--title-ink);
  }
  .backdrop {
    position: absolute;
    display: flex;
    overflow: hidden;
  }
  .backdrop--large {
    left: 251px;
    top: 182px;
    width: 705px;
    height: 523px;
    border-radius: 22px;
  }
  .backdrop--preview {
    left: 382px;
    top: 792px;
    width: 444px;
    height: 329px;
    border-radius: 14px;
  }
  .panel {
    width: 50%;
    height: 100%;
    display: block;
  }
  .panel-text { font-family: "Exo 2", sans-serif; }
  .dimension {
    position: absolute;
    font-family: "Open Sans", sans-serif;
    font-size: 18px;
    color: #111;
    margin: 0;
  }
  .dimension--left { left: 485px; top: 760px; }
  .dimension--right { left: 703px; top: 760px; }
  .dimension--height {
    left: 826px;
    top: 956px;
    transform: rotate(90deg);
  }
  .screen-stand {
    position: absolute;
    left: 349px;
    top: 977px;
    width: 120px;
    height: 160px;
  }
  .defs { position: absolute; width: 0; height: 0; }
</style>
</head>
<body>
<svg class="defs" aria-hidden="true">
  <defs>
    <symbol id="sparkle" viewBox="-10 -10 20 20">
      <path d="M0,-10 Q1.6,-1.6 10,0 Q1.6,1.6 0,10 Q-1.6,1.6 -10,0 Q-1.6,-1.6 0,-10 Z"/>
    </symbol>
    <linearGradient id="photo-tone" x1="0" y1="0" x2="1" y2="1">
      <stop offset="0" stop-color="#2b3138"/>
      <stop offset="0.35" stop-color="#5f6d7b"/>
      <stop offset="0.55" stop-color="#7a4a33"/>
      <stop offset="0.8" stop-color="#1f2b33"/>
      <stop offset="1" stop-color="#0f161b"/>
    </linearGradient>
  </defs>
</svg>

<main class="sheet">
  <h1 class="sheet-title">10 FT CONFIGURATION</h1>

  <!-- Large rendering of the two 5 ft panels -->
  <section class="backdrop backdrop--large">
    <svg class="panel panel--brand" viewBox="0 0 565 837" preserveAspectRatio="none">
      <rect width="565" height="837" fill="url(#photo-tone)" role="img" aria-label="Photo: mining worker in an orange hard hat and high-visibility jacket looking at monitors in a control room"/>
      <text class="panel-text" x="77" y="120" font-size="62" font-weight="700" fill="var(--white)" letter-spacing="2">STRATUM</text>
      <text class="panel-text" x="412" y="96" font-size="20" font-weight="600" fill="var(--white)">Mining</text>
      <text class="panel-text" x="412" y="120" font-size="20" font-weight="600" fill="var(--white)">Solution</text>
      <text class="panel-text" x="282" y="740" text-anchor="middle" font-size="46" font-weight="600" fill="var(--tagline)">Be The Standout.</text>
    </svg>
    <svg class="panel panel--services" viewBox="0 0 565 837" preserveAspectRatio="none">
      <rect width="565" height="837" fill="var(--brand-red)"/>
      <text class="panel-text" x="276" y="56" text-anchor="middle" font-size="28" font-weight="700" fill="var(--white)">Transformational Mining Solutions</text>
      <path d="M0,138 Q282,50 565,140 L565,560 C500,665 380,705 280,712 C150,722 40,750 0,805 Z" fill="var(--brand-grey)"/>
      <path d="M0,162 Q282,75 565,162 L565,530 C500,635 380,675 280,685 C150,695 40,725 0,780 Z" fill="var(--brand-navy)"/>
      <g fill="var(--brand-red)">
        <use href="#sparkle" x="56" y="196" width="40" height="40"/>
        <use href="#sparkle" x="56" y="274" width="40" height="40"/>
        <use href="#sparkle" x="56" y="353" width="40" height="40"/>
        <use href="#sparkle" x="56" y="430" width="40" height="40"/>
        <use href="#sparkle" x="56" y="507" width="40" height="40"/>
        <use href="#sparkle" x="56" y="584" width="40" height="40"/>
      </g>
      <g class="panel-text" font-size="28" font-weight="600" fill="var(--white)">
        <text x="109" y="226">Advanced Dispatch Program</text>
        <text x="107" y="304">Short Interval Control Solution</text>
        <text x="107" y="383">Business Improvement Training</text>
        <text x="105" y="460">Maintenance &amp; Reliability</text>
        <text x="107" y="537">Integrated Operations</text>
        <text x="109" y="614">SMS LEAD</text>
      </g>
      <g fill="var(--sparkle)">
        <use href="#sparkle" x="442" y="685" width="62" height="62"/>
        <use href="#sparkle" x="500" y="672" width="26" height="26"/>
        <use href="#sparkle" x="415" y="695" width="16" height="16"/>
        <use href="#sparkle" x="70" y="770" width="54" height="54"/>
        <use href="#sparkle" x="26" y="776" width="34" height="34"/>
      </g>
      <g class="panel-text" font-size="25" font-weight="600" fill="var(--white)">
        <text x="110" y="758">Comprehensive Solutions</text>
        <text x="165" y="789">Developed by Mining Experts</text>
      </g>
    </svg>
  </section>

  <p class="dimension dimension--left">5 ft</p>
  <p class="dimension dimension--right">5 ft</p>

  <!-- Scaled preview with screen stand -->
  <section class="backdrop backdrop--preview">
    <svg class="panel panel--brand" viewBox="0 0 565 837" preserveAspectRatio="none">
      <rect width="565" height="837" fill="url(#photo-tone)" role="img" aria-label="Photo: mining worker in an orange hard hat and high-visibility jacket looking at monitors in a control room"/>
      <text class="panel-text" x="77" y="120" font-size="62" font-weight="700" fill="var(--white)" letter-spacing="2">STRATUM</text>
      <text class="panel-text" x="412" y="96" font-size="20" font-weight="600" fill="var(--white)">Mining</text>
      <text class="panel-text" x="412" y="120" font-size="20" font-weight="600" fill="var(--white)">Solution</text>
      <text class="panel-text" x="282" y="740" text-anchor="middle" font-size="46" font-weight="600" fill="var(--tagline)">Be The Standout.</text>
    </svg>
    <svg class="panel panel--services" viewBox="0 0 565 837" preserveAspectRatio="none">
      <rect width="565" height="837" fill="var(--brand-red)"/>
      <text class="panel-text" x="276" y="56" text-anchor="middle" font-size="28" font-weight="700" fill="var(--white)">Transformational Mining Solutions</text>
      <path d="M0,138 Q282,50 565,140 L565,560 C500,665 380,705 280,712 C150,722 40,750 0,805 Z" fill="var(--brand-grey)"/>
      <path d="M0,162 Q282,75 565,162 L565,530 C500,635 380,675 280,685 C150,695 40,725 0,780 Z" fill="var(--brand-navy)"/>
      <g fill="var(--brand-red)">
        <use href="#sparkle" x="56" y="196" width="40" height="40"/>
        <use href="#sparkle" x="56" y="274" width="40" height="40"/>
        <use href="#sparkle" x="56" y="353" width="40" height="40"/>
        <use href="#sparkle" x="56" y="430" width="40" height="40"/>
        <use href="#sparkle" x="56" y="507" width="40" height="40"/>
        <use href="#sparkle" x="56" y="584" width="40" height="40"/>
      </g>
      <g class="panel-text" font-size="28" font-weight="600" fill="var(--white)">
        <text x="109" y="226">Advanced Dispatch Program</text>
        <text x="107" y="304">Short Interval Control Solution</text>
        <text x="107" y="383">Business Improvement Training</text>
        <text x="105" y="460">Maintenance &amp; Reliability</text>
        <text x="107" y="537">Integrated Operations</text>
        <text x="109" y="614">SMS LEAD</text>
      </g>
      <g fill="var(--sparkle)">
        <use href="#sparkle" x="442" y="685" width="62" height="62"/>
        <use href="#sparkle" x="500" y="672" width="26" height="26"/>
        <use href="#sparkle" x="415" y="695" width="16" height="16"/>
        <use href="#sparkle" x="70" y="770" width="54" height="54"/>
        <use href="#sparkle" x="26" y="776" width="34" height="34"/>
      </g>
      <g class="panel-text" font-size="25" font-weight="600" fill="var(--white)">
        <text x="110" y="758">Comprehensive Solutions</text>
        <text x="165" y="789">Developed by Mining Experts</text>
      </g>
    </svg>
  </section>

  <svg class="screen-stand" viewBox="0 0 120 160">
    <rect x="0" y="0" width="117" height="64" fill="#000"/>
    <text x="58" y="36" text-anchor="middle" font-family="Open Sans, sans-serif" font-size="8" fill="#2a2a2a">SCREEN 1</text>
    <rect x="54" y="64" width="4" height="90" fill="#000"/>
    <rect x="36" y="152" width="41" height="7" fill="#000"/>
  </svg>

  <p class="dimension dimension--height">7.5 ft</p>
</main>
</body>
</html>
```